Hearth & Keg Room requires web site design - Casual restaurant

Need website designed for re-branding of Restaurant based in Fort Morgan, Colorado. We offer a wide variety of American cuisine in a casual, rustic atmosphere. We're offering 16 craft beers on draft, as well as a full service bar, and modern, interesting menu selections in a friendly, fun and energetic environment, with an emphasis on superior customer service and high quality, locally sourced food. We are a family, and community service oriented establishment. The website design should convey a welcoming sense, "simplicity", yet sophisticated - without pretentiousness. The website should effectively convey our "home style" relaxed atmosphere, as well as our casual character.

Business Hours: Sunday - Thursday, 11am-10pm / Friday & Saturday, 11am-11am

The Dunlo Hearth & Keg Room
2736 Pennick Road
Fort Morgan, Colorado 80701
B: (970) 555-0173

WEBSITE ADDRESS: thedunlokegroom.com

Target Market(s)

Young Adults
Families
Blue and White Collar Americans
Senior Citizens
Small town location, appeal to everyone

Industry/Entity Type

American Restaurant

Contact Information for Business Card

Marcus T Ellery
Food & Beverage Director
2736 Pennick Road
B: (970) 555-0173
M: (231) 555-0148
mtellery@dunlokegroom.com
www.thedunlokegroom.com
***Use logo in uploaded files
***Open to single OR double sided
*** I will have additional names and information to add to this, for other employees.

Coding

Coded - Design and coding required

Number of Pages Required

5+ page

Font styles to use
Serif
Sans Serif
Decorative
Other font styles liked:
• Calafornian FB,

Requirements
Must have
• Home/Welcome Page
• Menu Page/Online Ordering Ready
• About Us/Contact Us page
• Catering/Private Events/Banquets Advertising section
• Ability to link to Facebook/TripAdvisor/Yelp/Instagram etc.
• Logo uploaded, reference for colors as well.
Nice to have
• About craft beer page
• Our Story/Bio section
• Photo Gallery
• Employment/Apply section
Should not have
• We are NOT a "fine dining" restaurant... think casual...

```html
<!DOCTYPE html>
<html lang="en">
<head>
<meta charset="utf-8">
<title>The Dunlo Hearth &amp; Keg Room</title>
<link rel="stylesheet" href="https://fonts.googleapis.com/css2?family=Lato:wght@300;400;700;900&family=Open+Sans:ital,wght@0,400;0,600;0,700;1,400&family=Oswald:wght@400&family=Yellowtail&display=swap">
<style>
:root{
  --maroon:#5b0605;
  --maroon-light:#6e1a16;
  --orange:#f46f16;
  --heading:#5a0e0e;
  --text:#8a8580;
  --ink:#2b2320;
  --page:#f8f6ee;
  --panel:#f5f2ea;
  --line:#d9d4ca;
  --white:#ffffff;
}
*{box-sizing:border-box;margin:0;padding:0}
html,body{width:1200px;height:2239px;overflow:hidden}
body{background:var(--page);font-family:"Open Sans",Arial,sans-serif;color:var(--text);font-size:13px}
a{color:inherit;text-decoration:none}
.site{position:relative;width:960px;height:2239px;margin:0 auto;background:var(--panel);box-shadow:0 0 6px rgba(0,0,0,.08)}

/* top bar */
.topbar{height:28px;background:var(--maroon);display:flex;justify-content:space-between;align-items:center;padding:0 43px;font-size:9px;color:#e8cfc8;text-transform:uppercase;letter-spacing:.3px}
.topbar nav a{margin-right:18px}
.topbar .info{display:flex;align-items:center;gap:14px}
.topbar .info b{color:#fff;font-weight:600}
.topbar .pill{background:var(--orange);color:#fff;padding:3px 8px;font-weight:700;letter-spacing:.6px}
.icon{width:10px;height:10px;vertical-align:-1px;margin-left:3px}

/* header */
.header{height:97px;display:flex;justify-content:space-between;align-items:center;padding:0 43px}
.brand{display:flex;align-items:center;gap:8px;font-family:"Lato",Arial,sans-serif;font-weight:900;font-size:32px;color:var(--ink);letter-spacing:-.5px}
.brand .mark{width:12px;height:12px;background:var(--orange)}
.mainnav{display:flex;gap:26px;font-family:"Oswald",Arial,sans-serif;font-size:12px;letter-spacing:1px;color:var(--ink);text-transform:uppercase}

/* hero */
.hero{margin:0 43px;height:372px;background:radial-gradient(circle at 62% 30%,#5a3a22 0%,#2a1b10 35%,#0e0906 70%);position:relative}
.hero .copy{position:absolute;left:38px;top:202px;color:#fff}
.hero h1{font-weight:400;font-size:40px;line-height:48px;letter-spacing:-.5px}
.hero h1 b{font-weight:700}
.hero p{font-size:13px;line-height:22px;color:#e9e2da;width:420px;margin-top:2px}

/* features */
.features{display:flex;gap:41px;padding:66px 43px 0;height:476px;overflow:hidden}
.feature{width:265px}
.thumb{height:164px;border:1px solid #ddd7cc;padding:5px;background:#fff}
.thumb div{height:100%}
.feature .kicker{font-style:italic;font-size:12px;line-height:18px;color:var(--orange);margin-top:14px}
.feature h2{font-family:"Lato",Arial,sans-serif;font-weight:700;font-size:26px;line-height:32px;color:var(--heading);margin-top:16px}
.feature .desc{font-size:12.5px;line-height:22px;margin-top:20px;height:66px}
.feature .desc b{color:#6c625c}
.btn{display:inline-block;font-size:10.5px;letter-spacing:1px;text-transform:uppercase;padding:8px 14px;border:1px solid var(--line);background:#fff;color:#4b403a;font-weight:600}
.feature .btn{margin-top:22px}
.btn.solid{background:var(--orange);border-color:var(--orange);color:#fff;font-weight:700}

/* menu banner */
.menu-banner{height:333px;background:linear-gradient(100deg,#3b2414 0%,#4a2e19 40%,#2a190d 100%);position:relative}
.menu-banner .script{position:absolute;left:40px;top:112px;font-family:"Yellowtail",cursive;font-size:54px;line-height:60px;color:var(--orange)}
.menu-banner .sub{position:absolute;left:42px;top:174px;font-weight:700;font-size:21px;letter-spacing:2px;color:#fff}

/* menu lists */
.menus{display:flex;gap:58px;padding:48px 43px 0;height:333px}
.menu-col{flex:1}
.menu-col h3{font-family:"Lato",Arial,sans-serif;font-weight:300;font-size:26px;line-height:32px;color:var(--heading);margin-bottom:24px}
.menu-col h3 b{font-weight:700}
.item{display:flex;gap:12px;height:66px}
.item .pic{width:36px;height:36px;flex:none;margin-top:6px}
.item .body{flex:1}
.item .name{font-size:14px;letter-spacing:1px;color:var(--orange);text-transform:uppercase;display:flex;align-items:center;gap:6px}
.tag{font-size:8px;font-weight:700;letter-spacing:.8px;background:var(--orange);color:#fff;padding:1px 5px}
.item .desc{display:flex;align-items:baseline;font-size:12.5px;margin-top:4px}
.item .dots{flex:1;border-bottom:2px dotted #7a706a;margin:0 4px}
.item .price{color:#6c625c}
.discover{text-align:center}
.discover .btn{padding:13px 20px}

/* newsletter */
.connect{display:flex;justify-content:space-between;align-items:flex-start;padding:22px 43px 0;height:133px}
.newsletter{display:flex;align-items:center;gap:14px}
.label{font-size:13px;letter-spacing:2px;text-transform:uppercase;color:var(--ink)}
.newsletter input{width:152px;height:33px;border:1px solid var(--line);padding:0 10px;font-size:10px;font-family:inherit;background:#fff}
.newsletter .btn{margin-left:-10px;padding:9px 10px;font-size:10px}
.follow{display:flex;align-items:center;gap:8px}
.follow .label{margin-right:12px}
.social{width:31px;height:31px;border-radius:50%;background:#111;display:flex;align-items:center;justify-content:center}

/* footer */
.footer{position:absolute;left:0;top:1772px;width:960px;height:467px;background:var(--maroon);color:#e8cfc8}
.footer .cols{display:flex;gap:41px;padding:48px 43px 0;height:385px}
.footer .col{width:265px}
.footer h4{font-family:"Lato",Arial,sans-serif;font-weight:700;font-size:13px;letter-spacing:1.5px;color:#fff;margin-bottom:28px}
.footer .photo{height:108px}
.contact{list-style:none;margin-top:22px;font-size:12px;line-height:20px}
.contact li{display:flex;gap:22px;margin-bottom:10px}
.contact svg{width:11px;height:11px;margin-top:4px;flex:none}
.contact a{color:var(--orange)}
.links{list-style:none;font-size:12px;color:var(--orange)}
.links li{height:36px;border-bottom:1px solid rgba(255,255,255,.08);padding-top:8px}
.links li::before{content:"›";color:#e8cfc8;margin-right:10px}
.news{display:flex;align-items:center;gap:14px;height:73px;padding:0 15px;font-size:12px;color:var(--orange)}
.news.shade{background:var(--maroon-light)}
.news .pic{width:43px;height:43px;flex:none}
.footer .bottom{margin:0 43px;border-top:1px solid rgba(255,255,255,.12);display:flex;justify-content:space-between;padding-top:44px;font-size:11px}
.footer .bottom nav{display:flex;gap:12px;color:var(--orange)}
.footer .bottom .copy{color:var(--orange)}
</style>
</head>
<body>
<div class="site">

  <div class="topbar">
    <nav><a href="#">About us</a><a href="#">Latest news</a><a href="#">Quick order</a><a href="#">Gallery</a></nav>
    <div class="info">
      <span>2736 Pennick Road <b>View on map</b><svg class="icon" viewBox="0 0 10 10"><path d="M5 0a3.5 3.5 0 0 0-3.5 3.5C1.5 6 5 10 5 10s3.5-4 3.5-6.5A3.5 3.5 0 0 0 5 0zm0 5a1.5 1.5 0 1 1 0-3 1.5 1.5 0 0 1 0 3z" fill="#fff"/></svg></span>
      <span>Call us: <b>(970) 555-0173</b><svg class="icon" viewBox="0 0 10 10"><rect width="10" height="10" rx="1.5" fill="#fff"/><path d="M3 2l1 1.6-.7.7a5 5 0 0 0 2.4 2.4l.7-.7L8 7v1C4.5 8 2 5.5 2 2z" fill="#5b0605"/></svg></span>
      <a class="pill" href="#">Reservation</a>
    </div>
  </div>

  <header class="header">
    <a class="brand" href="#"><span class="mark"></span>The Dunlo</a>
    <nav class="mainnav"><a href="#">Home</a><a href="#">About us</a><a href="#">Menu</a><a href="#">Events</a><a href="#">Reservation</a><a href="#">Reviews</a><a href="#">Contact</a></nav>
  </header>

  <section class="hero" role="img" aria-label="Wine bottle and glass beside an oak barrel with green grapes">
    <div class="copy">
      <h1>THE <b>DUNLO Hearth &amp; Keg Room</b></h1>
      <p>A lovely place to meet a friend and chat over lunch, served in a pleasant little room with wonderful omelets and salads and such.</p>
    </div>
  </section>

  <section class="features">
    <article class="feature">
      <div class="thumb"><div role="img" aria-label="Chefs in white uniforms preparing food" style="background:linear-gradient(135deg,#3f4a3a,#b9b3a6 55%,#5c4a3a)"></div></div>
      <p class="kicker">The Executive Chef</p>
      <h2>RAMON KESSLER</h2>
      <p class="desc">Ramon was honest and smart and had the highest personal integrity of anyone I have ever known about people.</p>
      <a class="btn" href="#">View our chefs</a>
    </article>
    <article class="feature">
      <div class="thumb"><div role="img" aria-label="Restaurant front with lit sign at night" style="background:linear-gradient(160deg,#2a2f4a,#b2532a 55%,#1f1a22)"></div></div>
      <p class="kicker">The Best Of Colorado</p>
      <h2>RESTAURANT</h2>
      <p class="desc"><b>Phone:</b> (970) 555-0173<br><b>Address:</b>2736 Pennick Road<br>Fort Morgan, Colorado 80701</p>
      <a class="btn" href="#">More about us</a>
    </article>
    <article class="feature">
      <div class="thumb"><div role="img" aria-label="Bright dining room with set tables" style="background:linear-gradient(180deg,#c9c2b0,#ece8df 55%,#8e8a82)"></div></div>
      <p class="kicker">The Reservation</p>
      <h2>DINING ROOM</h2>
      <p class="desc">The dining room by nature is simple space. Unlike a kitchen or living room, which often has multiple purposes.</p>
      <a class="btn solid" href="#">Make a reservation »</a>
    </article>
  </section>

  <section class="menu-banner" role="img" aria-label="Red wine bottle and glasses on a dark wooden table">
    <div class="script">Restaurant Menu</div>
    <div class="sub">YOUR FRIENDS WILL LOVE</div>
  </section>

  <section class="menus">
    <div class="menu-col">
      <h3>NEW YEAR <b>2017</b></h3>
      <div class="item"><div class="pic" role="img" aria-label="Foie gras dish" style="background:linear-gradient(135deg,#8a6a4a,#e2d6c0)"></div>
        <div class="body"><div class="name">Foie Gras Ballotine <span class="tag">POPULAR</span></div>
        <div class="desc">Grilled Celery Blue Mountain<span class="dots"></span><span class="price">$36</span></div></div></div>
      <div class="item"><div class="pic" role="img" aria-label="Cannelloni dish" style="background:linear-gradient(135deg,#6a4a2a,#d9b58a)"></div>
        <div class="body"><div class="name">Sweetbread and Porcini Cannelloni</div>
        <div class="desc">Alba White Truffle, Robiolo Emulsion<span class="dots"></span><span class="price">$22</span></div></div></div>
      <div class="item"><div class="pic" role="img" aria-label="Abalone dish" style="background:linear-gradient(135deg,#4a5a2a,#b7854a)"></div>
        <div class="body"><div class="name">Jade Tiger Abalone</div>
        <div class="desc">Fingerling Potatoes, Ossetra Caviar<span class="dots"></span><span class="price">$10</span></div></div></div>
    </div>
    <div class="menu-col">
      <h3>SPECIAL FOR <b>PARTY</b></h3>
      <div class="item"><div class="pic" role="img" aria-label="Lobster salad" style="background:linear-gradient(135deg,#5a6a2a,#d8c08a)"></div>
        <div class="body"><div class="name">Maine Lobster Salad</div>
        <div class="desc">Hawaiian Hearts of Palm, Romaine Lettuce<span class="dots"></span><span class="price">$22</span></div></div></div>
      <div class="item"><div class="pic" role="img" aria-label="Langoustines dish" style="background:linear-gradient(135deg,#3a4a3a,#b6a78a)"></div>
        <div class="body"><div class="name">Crispy Scottish Langoustines</div>
        <div class="desc">Glazed Sunchoke, Parsley Salad<span class="dots"></span><span class="price">$10</span></div></div></div>
      <div class="item"><div class="pic" role="img" aria-label="Oysters on a plate" style="background:linear-gradient(135deg,#6a5a4a,#e3d9c9)"></div>
        <div class="body"><div class="name">Chilled Shigoku Oysters <span class="tag">CHEF SELECTION</span></div>
        <div class="desc">Fennel Mousseline, Sea Urchin, Finger Lime<span class="dots"></span><span class="price">$10</span></div></div></div>
    </div>
  </section>

  <div class="discover"><a class="btn" href="#">Discover our menu »</a></div>

  <section class="connect">
    <form class="newsletter">
      <span class="label">Newsletter</span>
      <input type="email" placeholder="Enter your e-mail address">
      <a class="btn" href="#">Subscribe</a>
    </form>
    <div class="follow">
      <span class="label">Follow us</span>
      <a class="social" href="#" aria-label="Social link"></a>
      <a class="social" href="#" aria-label="Social link"></a>
      <a class="social" href="#" aria-label="Social link"></a>
      <a class="social" href="#" aria-label="Social link"></a>
      <a class="social" href="#" aria-label="Email"><svg width="13" height="10" viewBox="0 0 13 10"><rect width="13" height="10" rx="1" fill="#fff"/><path d="M0.5 1l6 4.5 6-4.5" fill="none" stroke="#111" stroke-width="1.2"/></svg></a>
    </div>
  </section>

  <footer class="footer">
    <div class="cols">
      <div class="col">
        <h4>THE DUNLO</h4>
        <div class="photo" role="img" aria-label="Restaurant front lit at night" style="background:linear-gradient(160deg,#2a2f4a,#b2532a 55%,#1f1a22)"></div>
        <ul class="contact">
          <li><svg viewBox="0 0 10 10"><path d="M5 0a3.5 3.5 0 0 0-3.5 3.5C1.5 6 5 10 5 10s3.5-4 3.5-6.5A3.5 3.5 0 0 0 5 0zm0 5a1.5 1.5 0 1 1 0-3 1.5 1.5 0 0 1 0 3z" fill="#fff"/></svg><span>2736 Pennick Road<br>Fort Morgan, Colorado 80701</span></li>
          <li><svg viewBox="0 0 10 10"><path d="M2 0l2 2.5-1 1.2a6 6 0 0 0 3.3 3.3l1.2-1L10 8 8.5 10C4 10 0 6 0 1.5z" fill="#fff"/></svg><span>(970) 555-0173</span></li>
          <li><svg viewBox="0 0 10 10"><rect y="1.5" width="10" height="7" fill="#fff"/><path d="M0 2l5 3.5L10 2" fill="none" stroke="#5b0605"/></svg><a href="#">contact@thedunlokegroom.com</a></li>
        </ul>
      </div>
      <div class="col">
        <h4>SITE LINKS</h4>
        <ul class="links">
          <li>About Us</li><li>Reservation</li><li>Events</li><li>Online Booking</li><li>Contact Us</li><li>Privacy Policy</li>
        </ul>
      </div>
      <div class="col">
        <h4>RECENT NEWS</h4>
        <div class="news shade"><div class="pic" role="img" aria-label="Healthy food plate" style="background:linear-gradient(135deg,#3a2a1a,#c0542a)"></div>Food For Healthy Living</div>
        <div class="news"><div class="pic" role="img" aria-label="Duck dish with plums" style="background:linear-gradient(135deg,#e6ddd0,#a4402a)"></div>Portuguese Plum Duck Food</div>
        <div class="news shade"><div class="pic" role="img" aria-label="Turkey dish" style="background:linear-gradient(135deg,#6a4a2a,#d8b07a)"></div>Top Turkey Dishes in Chicago</div>
      </div>
    </div>
    <div class="bottom">
      <span class="copy">Copyright © 2017 The Dunlo .</span>
      <nav><a href="#">Online Booking</a><a href="#">About Us</a><a href="#">Contact Us</a><a href="#">Privacy Policy</a><a href="#">Terms of Use</a></nav>
    </div>
  </footer>

</div>
</body>
</html>
```